依頼詳細
安くて簡単に発注が出来ることをアピールしたいと思っております。
記載項目
ラフを添付しておりますのでご確認ください。配置や文章などより分かりやすいデザインがある場合はラフ通りでなくても問題ございません。あくまで素人がラフを作成しましたので・・ラフはモノクロですがカラーの明るいイメージでお願いします

また納期がタイトなため、日曜日までの受付とさせていただき、月曜日にデータ納品が出来る方でお願いします。
サイズ
A4
ページ数
両面
希望イメージ
シンプル 複雑
単色 カラフル
暗い 明るい
日常 高級
遊び心 厳粛
未来的 伝統的
女性的 男性的
希望する色
弊社サイトがオレンジの為、オレンジと白を基調にお願いします。
納品ファイル
• 高解像度JPG (.jpg)
• イラストレーター形式 (.ai)
補足説明
弊社サイトは下記URLになります。
http://krvprint.net
選定確約に変更させて頂きます。

また、月曜日までの納品は必須になってしまいますので、修正がある場合などは締め切り時間(7月7日の18時頃)30分後までには修正依頼をお願いすることになります。修正を依頼するのは確定する方1名とさせて頂きます。

修正が完了されましたら完了したデータを納品して頂ければ確定させて頂きます。
納期タイトで大変申し訳ございませんが多くの応募をお待ちしております。

```html
<!DOCTYPE html>
<html lang="ja">
<head>
<meta charset="utf-8">
<title>名刺が簡単に安く発注できます</title>
<link href="https://fonts.googleapis.com/css2?family=Noto+Sans+JP:wght@400;700;900&display=swap" rel="stylesheet">
<style>
:root{
  --orange:#f26b1d;
  --white:#ffffff;
  --ink:#222222;
  --grey:#666666;
  --line:#dddddd;
  --blue:#2a8fd6;
  --green:#36b24a;
  --yellow:#e9b51c;
  --purple:#b04fb8;
  --red:#e23a3a;
}
*{margin:0;padding:0;box-sizing:border-box}
html,body{width:859px;height:1200px;overflow:hidden;background:var(--white)}
body{font-family:"Noto Sans JP",sans-serif;color:var(--ink);position:relative}
.headline{position:absolute;left:0;top:40px;width:859px;text-align:center;font-weight:900;line-height:1.2}
.headline .line{display:block;font-size:82px;letter-spacing:2px}
.headline .accent{color:var(--orange);font-size:116px;letter-spacing:4px;line-height:1.1}
.panel{position:absolute;left:0;top:415px;width:859px;height:725px;background:var(--orange)}
.box{position:absolute;background:var(--white);border-radius:6px}
.tab{position:absolute;left:14px;top:-14px;background:var(--orange);color:var(--white);font-weight:700;font-size:20px;padding:4px 14px;border:3px solid var(--white);border-radius:4px;white-space:nowrap}
.bullet{font-weight:700;font-size:19px;white-space:nowrap}
.bullet::before{content:"● ";color:var(--orange)}
.price-box{left:63px;top:25px;width:747px;height:228px}
.price-box .bullet{position:absolute;left:24px;top:30px}
.prices{position:absolute;left:24px;top:68px;display:flex;gap:10px}
.price-card{width:134px;height:140px;border:2px solid var(--line);border-radius:4px;text-align:center;overflow:hidden;display:flex;flex-direction:column}
.price-card .kind{color:var(--white);font-size:13px;font-weight:700;padding:5px 0;white-space:nowrap}
.price-card .amount{display:flex;align-items:baseline;justify-content:center;gap:3px;font-weight:900;font-size:40px;color:var(--orange);margin-top:16px;line-height:1}
.price-card .amount small{font-size:13px;color:var(--orange);font-weight:700}
.price-card .note{font-size:12px;color:var(--grey);margin-top:14px}
.exhibit-box{left:63px;top:263px;width:747px;height:232px}
.exhibit-box .bullet{position:absolute;left:24px;top:34px}
.fee{position:absolute;left:34px;top:74px;font-size:17px;color:var(--grey);white-space:nowrap}
.free-edit{position:absolute;left:34px;top:112px;font-size:16px;line-height:1.5;white-space:nowrap}
.free-edit b{color:var(--orange);font-size:20px}
.small-note{position:absolute;left:34px;top:190px;font-size:11px;color:var(--grey);white-space:nowrap}
.zero-arrow{position:absolute;left:410px;top:84px}
.zero{position:absolute;left:560px;top:40px;width:170px;height:110px;border:3px solid var(--orange);border-radius:6px;color:var(--orange);font-weight:900;font-size:64px;text-align:center;line-height:104px}
.shipping-box{left:63px;top:507px;width:407px;height:160px}
.ship-list{position:absolute;left:30px;top:40px;list-style:none;font-size:15px;line-height:2;white-space:nowrap}
.ship-list li::before{content:"● ";color:var(--orange)}
.ship-list span{color:var(--grey)}
.next-arrow{position:absolute;left:487px;top:500px}
.next-label{position:absolute;left:505px;top:560px;color:var(--orange);font-weight:900;font-size:32px;white-space:nowrap}
.footer{position:absolute;left:0;top:1140px;width:859px;height:60px}
.brand{position:absolute;left:40px;top:10px;display:flex;align-items:center;gap:10px}
.brand-mark{width:40px;height:40px;background:var(--orange)}
.brand-name{font-weight:700;font-size:22px;color:var(--orange);line-height:1}
.brand-sub{font-size:12px;color:var(--ink)}
.contact{position:absolute;left:430px;top:4px;font-size:14px;line-height:1.35;color:var(--ink)}
</style>
</head>
<body>
<h1 class="headline">
  <span class="line">名刺が</span>
  <span class="line accent">簡単に安く</span>
  <span class="line">発注できます !!</span>
</h1>

<section class="panel">
  <div class="box price-box">
    <div class="tab">業界最安値に挑戦！</div>
    <p class="bullet">Linea Studio データでの入稿価格</p>
    <div class="prices">
      <div class="price-card"><div class="kind" style="background:var(--blue)">片面モノクロ</div><div class="amount"><small>税込</small>¥160</div><div class="note">上質紙100枚</div></div>
      <div class="price-card"><div class="kind" style="background:var(--green)">両面モノクロ</div><div class="amount"><small>税込</small>¥290</div><div class="note">上質紙100枚</div></div>
      <div class="price-card"><div class="kind" style="background:var(--yellow)">片面カラー</div><div class="amount"><small>税込</small>¥390</div><div class="note">上質紙100枚</div></div>
      <div class="price-card"><div class="kind" style="background:var(--purple)">表カラー裏モノクロ</div><div class="amount"><small>税込</small>¥490</div><div class="note">上質紙100枚</div></div>
      <div class="price-card"><div class="kind" style="background:var(--red)">両面カラー</div><div class="amount"><small>税込</small>¥590</div><div class="note">上質紙100枚</div></div>
    </div>
  </div>

  <div class="box exhibit-box">
    <div class="tab">展示会サービス</div>
    <p class="bullet">現物名刺からのデータ作成料</p>
    <p class="fee">データ作成料：<s>片面2,000円 両面3,000円</s></p>
    <p class="free-edit">しかも１度弊社で作成されたデザインの<br><b>文字修正無料！</b></p>
    <p class="small-note">※ただしデザイン変更は別途ご相談ください</p>
    <svg class="zero-arrow" width="130" height="60" viewBox="0 0 130 60"><path d="M0 27h105v-14l25 17-25 17v-14H0z" fill="var(--orange)"/></svg>
    <div class="zero">0円</div>
  </div>

  <div class="box shipping-box">
    <div class="tab">他にかかる費用は送料のみ</div>
    <ul class="ship-list">
      <li>ミドリメール便・・・・・<span>税込</span> ¥180</li>
      <li>ミドリ速達メール便・・・<span>税込</span> ¥290</li>
      <li>アオバ宅配便・・・・・・<span>税込</span> ¥650</li>
    </ul>
  </div>

  <svg class="next-arrow" width="330" height="170" viewBox="0 0 330 170"><path d="M0 25h250V0l80 85-80 85v-25H0z" fill="var(--white)"/></svg>
  <p class="next-label">発注方法は裏面へ</p>
</section>

<footer class="footer">
  <div class="brand">
    <div class="brand-mark"></div>
    <div>
      <div class="brand-sub">名刺印刷なら</div>
      <div class="brand-name">クルブデザイン</div>
    </div>
  </div>
  <div class="contact">
    〒100-0000 東京都架空市緑町1-2-3<br>
    mail：info@krvprint.net<br>
    http://krvprint.net
  </div>
</footer>
</body>
</html>
```